Business card design needed for elearning/LMS consultant

I'm an elearning and learning management system (LMS) consultant that requires a minimalist, technology/cutting edge, business card. I do not have a logo or colour scheme. I offer clients hands on expertise in 'elearning authouring', 'LMS ecosystems', 'elearning strategy', 'technical implementation', 'mlearning', 'LMS evaluation', 'big data', 'learner analytics' and 'reporting strategy', 'social learning', 'elearning blueprint'. I'm thinking a 'tag cloud' of the above services on the back of the card, with contact details on front, but unsure if it's passe so please don't let it constrain you.

Target Market(s)

C-level executives, learning and development senior management,

Industry/Entity Type

Business

Contact Information for Business Card

Owen Haldric
owen.haldric@mailvane.net
0412 836 197

Requirements
Should not have
• cheesy headshots, overused stockphotos, CLIPART and comic sans ;)

```html
<!DOCTYPE html>
<html lang="en">
<head>
<meta charset="utf-8">
<title>Services Tag Cloud</title>
<link rel="stylesheet" href="https://fonts.googleapis.com/css2?family=Itim&display=swap">
<style>
  :root {
    --navy: #1f3461;
    --grid: rgba(255, 255, 255, 0.05);
    --white: #ffffff;
    --green: #3fae3a;
    --pink: #d9286f;
    --tan: #b77a52;
    --yellow: #e6f20a;
  }
  html, body {
    margin: 0;
    padding: 0;
    width: 1200px;
    height: 695px;
    overflow: hidden;
  }
  .card {
    position: relative;
    width: 1200px;
    height: 695px;
    overflow: hidden;
    background-color: var(--navy);
    background-image:
      linear-gradient(var(--grid) 1px, transparent 1px),
      linear-gradient(90deg, var(--grid) 1px, transparent 1px);
    background-size: 10px 10px;
  }
  .tag-cloud {
    display: block;
    width: 1200px;
    height: 695px;
    font-family: "Itim", "Comic Neue", sans-serif;
  }
  .tag--white { fill: var(--white); }
  .tag--green { fill: var(--green); }
  .tag--pink { fill: var(--pink); }
  .tag--tan { fill: var(--tan); }
  .tag--yellow { fill: var(--yellow); }
</style>
</head>
<body>
<main class="card">
  <svg class="tag-cloud" viewBox="0 0 1062 615" role="list" aria-label="Consulting services">
    <!-- horizontal tags -->
    <text class="tag tag--green" x="415" y="68" font-size="38" textLength="262" lengthAdjust="spacingAndGlyphs">reporting strategy</text>
    <text class="tag tag--white" x="722" y="82" font-size="17" textLength="108" lengthAdjust="spacingAndGlyphs">mobile learning</text>
    <text class="tag tag--white" x="343" y="108" font-size="21" textLength="125" lengthAdjust="spacingAndGlyphs">social learning</text>
    <text class="tag tag--pink" x="502" y="105" font-size="27" textLength="85" lengthAdjust="spacingAndGlyphs">big data</text>
    <text class="tag tag--white" x="610" y="115" font-size="22" textLength="175" lengthAdjust="spacingAndGlyphs">e-learning authoring</text>
    <text class="tag tag--yellow" x="145" y="142" font-size="21" textLength="140" lengthAdjust="spacingAndGlyphs">LMS ecosystem</text>
    <text class="tag tag--tan" x="385" y="162" font-size="40" textLength="443" lengthAdjust="spacingAndGlyphs">LMS technical implementation</text>
    <text class="tag tag--white" x="175" y="220" font-size="60" textLength="650" lengthAdjust="spacingAndGlyphs">LMS evaluation and selection</text>
    <text class="tag tag--pink" x="80" y="285" font-size="57" textLength="418" lengthAdjust="spacingAndGlyphs">e-learning strategy</text>
    <text class="tag tag--white" x="615" y="265" font-size="29" textLength="275" lengthAdjust="spacingAndGlyphs">LMS project management</text>
    <text class="tag tag--white" x="645" y="302" font-size="21" textLength="157" lengthAdjust="spacingAndGlyphs">reporting strategy</text>
    <text class="tag tag--yellow" x="610" y="352" font-size="54" textLength="370" lengthAdjust="spacingAndGlyphs">learner analytics</text>
    <text class="tag tag--white" x="205" y="350" font-size="38" textLength="297" lengthAdjust="spacingAndGlyphs">e-learning authoring</text>
    <text class="tag tag--white" x="237" y="391" font-size="22" textLength="226" lengthAdjust="spacingAndGlyphs">LMS project management</text>
    <text class="tag tag--green" x="643" y="397" font-size="22" textLength="262" lengthAdjust="spacingAndGlyphs">LMS technical implementation</text>
    <text class="tag tag--green" x="376" y="440" font-size="20" textLength="167" lengthAdjust="spacingAndGlyphs">e-learning blueprint</text>
    <text class="tag tag--white" x="643" y="440" font-size="38" textLength="209" lengthAdjust="spacingAndGlyphs">social learning</text>
    <text class="tag tag--tan" x="363" y="482" font-size="28" textLength="172" lengthAdjust="spacingAndGlyphs">LMS ecosystem</text>
    <text class="tag tag--white" x="388" y="513" font-size="22" textLength="84" lengthAdjust="spacingAndGlyphs">mlearning</text>
    <text class="tag tag--white" x="678" y="472" font-size="18" textLength="145" lengthAdjust="spacingAndGlyphs">e-learning authoring</text>

    <!-- tags reading upward -->
    <text class="tag tag--white" transform="translate(333 165) rotate(-90)" font-size="26" textLength="107" lengthAdjust="spacingAndGlyphs">mlearning</text>
    <text class="tag tag--white" transform="translate(528 408) rotate(-90)" font-size="18" textLength="168" lengthAdjust="spacingAndGlyphs">e-learning strategy</text>
    <text class="tag tag--white" transform="translate(585 570) rotate(-90)" font-size="46" textLength="333" lengthAdjust="spacingAndGlyphs">mobile learning</text>
    <text class="tag tag--tan" transform="translate(622 578) rotate(-90)" font-size="26" textLength="205" lengthAdjust="spacingAndGlyphs">e-learning blueprint</text>
    <text class="tag tag--white" transform="translate(351 535) rotate(-90)" font-size="18" textLength="131" lengthAdjust="spacingAndGlyphs">mobile learning</text>
    <text class="tag tag--yellow" transform="translate(514 570) rotate(-90)" font-size="16" textLength="72" lengthAdjust="spacingAndGlyphs">mlearning</text>
    <text class="tag tag--white" transform="translate(662 520) rotate(-90)" font-size="20" textLength="67" lengthAdjust="spacingAndGlyphs">big data</text>

    <!-- tags reading downward -->
    <text class="tag tag--pink" transform="translate(854 48) rotate(90)" font-size="27" textLength="172" lengthAdjust="spacingAndGlyphs">learner analytics</text>
    <text class="tag tag--white" transform="translate(904 80) rotate(90)" font-size="18" textLength="215" lengthAdjust="spacingAndGlyphs">LMS evaluation and selection</text>
  </svg>
</main>
</body>
</html>
```